New Business Card Design Project

Updated business card design. I am moving towards more coaching of, for the most part women, who are searching for more in their lives. I am an intuitive healer, homeopath and nutritionist but also an author and motivational speaker. Int the past I have included my photo on the card but that is not essential. My book is called the Brilliance of Saffron - Reclaiming the Shade of Your Spirit so my colours are typically magenta.
Target Market(s)
Women - 35 - 60 considering improving their health. However, I am also a professional speaker with a target audience including corporate and conferences.
Industry/Entity Type
Health And Wellness
Contact Information for Business Card
Lucinda Parvell, CNP, BSc
www.lucindaparvell.com
lucinda@lucindaparvell.com
519-362-7015
Facebook, instagram and twitter logos
Look and feel
Each slider illustrates characteristics of the customer's brand and the style your logo design should communicate.

```html
<!DOCTYPE html>
<html lang="en">
<head>
<meta charset="utf-8">
<title>Lucinda Parvell – Business Cards</title>
<link href="https://fonts.googleapis.com/css2?family=Roboto:wght@300;400;700&display=swap" rel="stylesheet">
<style>
  :root {
    --magenta: #e8368f;
    --ink: #2a2a2a;
    --card-black: #1f1d1e;
    --paper: #ffffff;
    --stage: #ecebe8;
    --text-light: #f2f2f2;
  }
  * { box-sizing: border-box; margin: 0; padding: 0; }
  html, body {
    width: 1200px; height: 950px; overflow: hidden;
    background: var(--stage);
    font-family: "Roboto", Arial, sans-serif;
  }
  .canvas { position: relative; width: 1200px; height: 950px; }

  .card {
    position: absolute;
    width: 620px; height: 354px;
    background: var(--paper);
    border-radius: 6px;
    overflow: hidden;
    box-shadow: 0 6px 22px rgba(0,0,0,.18);
  }
  .card--front { left: 60px; top: 70px; }
  .card--back  { left: 520px; top: 520px; border-radius: 18px; }

  /* Brand name set in the card's text font */
  .brand-name {
    color: var(--ink);
    font-weight: 300;
    white-space: nowrap;
    line-height: 1;
  }
  .tagline {
    color: var(--ink);
    font-weight: 400;
    letter-spacing: 1px;
    white-space: nowrap;
  }

  /* Front */
  .front__brand {
    position: absolute; right: 48px; top: 56px;
    display: flex; flex-direction: column; align-items: flex-end; gap: 16px;
  }
  .front__brand .brand-name { font-size: 46px; }
  .front__brand .tagline { font-size: 19px; }

  .front__wave { position: absolute; inset: 0; }

  .contact {
    position: absolute; left: 42px; top: 216px;
  }
  .contact__name {
    color: var(--magenta); font-weight: 700; font-size: 24px; line-height: 1;
  }
  .contact__creds {
    color: var(--magenta); font-size: 13px; margin-top: 6px;
  }
  .contact__list { list-style: none; margin-top: 10px; }
  .contact__item {
    display: flex; align-items: center; gap: 10px;
    color: var(--text-light); font-size: 14px; line-height: 22px;
  }
  .contact__icon { width: 14px; height: 14px; flex: none; }

  /* Back */
  .back__photo {
    position: absolute; left: 0; top: 0; width: 100%; height: 70%;
    background: linear-gradient(110deg, #4c5a3a 0%, #6d5a4a 35%, #c9a688 60%, #d8bf9e 100%);
  }
  .back__band {
    position: absolute; left: 0; bottom: 0; width: 100%; height: 30%;
    background: var(--paper);
    display: flex; flex-direction: column; align-items: center; justify-content: center; gap: 10px;
  }
  .back__band .brand-name { font-size: 36px; }
  .back__meta { display: flex; align-items: center; gap: 22px; }
  .back__meta .tagline { font-size: 15px; }
  .social { display: flex; gap: 6px; }
  .social__dot { width: 20px; height: 20px; border-radius: 50%; background: var(--ink); }
  .back__rule {
    width: 200px; height: 2px; background: var(--magenta);
  }
</style>
</head>
<body>
<main class="canvas">

  <section class="card card--front" aria-label="Business card front">
    <svg class="front__wave" viewBox="0 0 620 354" preserveAspectRatio="none" aria-hidden="true">
      <path d="M0,186 C180,176 420,214 620,318 L620,354 L0,354 Z" fill="var(--magenta)"/>
      <path d="M0,194 C180,184 420,222 620,326 L620,354 L0,354 Z" fill="var(--card-black)"/>
    </svg>

    <div class="front__brand">
      <div class="brand-name">Lucinda Parvell</div>
      <div class="tagline">vitality maverick</div>
    </div>

    <div class="contact">
      <div class="contact__name">Lucinda Parvell</div>
      <div class="contact__creds">CNP, BSc</div>
      <ul class="contact__list">
        <li class="contact__item">
          <svg class="contact__icon" viewBox="0 0 16 16" aria-hidden="true"><path d="M3 1l3 3-1.6 2a9 9 0 0 0 5.6 5.6L12 10l3 3-2 2C7 15 1 9 1 3z" fill="var(--magenta)"/></svg>
          <span>519-362-7015</span>
        </li>
        <li class="contact__item">
          <svg class="contact__icon" viewBox="0 0 16 16" aria-hidden="true"><rect x="1" y="3" width="14" height="10" rx="1" fill="var(--magenta)"/><path d="M1.5 3.5L8 9l6.5-5.5" stroke="var(--card-black)" stroke-width="1.4" fill="none"/></svg>
          <span>lucinda@lucindaparvell.com</span>
        </li>
        <li class="contact__item">
          <svg class="contact__icon" viewBox="0 0 16 16" aria-hidden="true"><circle cx="8" cy="8" r="7" fill="var(--magenta)"/><path d="M1 8h14M8 1c-3 3.5-3 10.5 0 14M8 1c3 3.5 3 10.5 0 14" stroke="var(--card-black)" stroke-width="1.1" fill="none"/></svg>
          <span>www.lucindaparvell.com</span>
        </li>
      </ul>
    </div>
  </section>

  <section class="card card--back" aria-label="Business card back">
    <div class="back__photo" role="img" aria-label="Portrait photograph of the coach in a white top standing against a brick wall beside greenery"></div>
    <div class="back__band">
      <div class="brand-name">Lucinda Parvell</div>
      <div class="back__meta">
        <div class="tagline">vitality maverick</div>
        <div class="social" aria-label="Social media profiles">
          <span class="social__dot"></span><span class="social__dot"></span><span class="social__dot"></span>
        </div>
      </div>
      <div class="back__rule"></div>
    </div>
  </section>

</main>
</body>
</html>
```